Business Card design for a skin clinic

i would like a business card design for our skin clinic.
our logo colors are Blue and Grey and Bule /white.
we are searching for a minimalistic design yet very elegant,dynamic and professional which can reflect a professional medical skin care clinic( not a beauty salon).
THE DESGIN IS NOT FOR A PERSON IT WILL BE USED IN THE CLINIC FOR CLIENTS SO THERE SHOULD BE NO NAME OF A PERSON ONLY THE CLINIC NAME AND THE CONTACT INFO

Target Market(s)
young and old womens
Industry/Entity Type
Business
Contact Information for Business Card
we have 2 address and both should be on the card.
address A: Lindenhofkade 42B, 3017KP Rotterdam, Tel 010 438 21 95
address B: Zonnewijzerstraat 73, 1062HT Amsterdam Tel 020 519 8372
website www.velorahuid.nu, email info@velorahuid.nu
Look and feel

```html
<!DOCTYPE html>
<html lang="nl">
<head>
<meta charset="utf-8">
<title>Velora Huid – Visitekaartje</title>
<link rel="stylesheet" href="https://fonts.googleapis.com/css2?family=Jost:wght@400;500&display=swap">
<style>
  :root {
    --backdrop: #d9d6d3;
    --card-dark: #1d2024;
    --card-light: #eeeeee;
    --silver: #9a9ea3;
    --silver-soft: #6f7378;
    --brand-blue: #2f7fc8;
    --ink: #55585c;
    --skin-warm: #e6d8d0;
  }
  * { box-sizing: border-box; margin: 0; padding: 0; }
  html, body {
    width: 1200px; height: 864px; overflow: hidden;
    background: var(--backdrop);
    font-family: "Jost", sans-serif;
  }
  .sheet {
    position: relative; width: 1200px; height: 864px;
  }
  .card {
    position: absolute; top: 262px;
    width: 545px; height: 340px;
    box-shadow: 0 10px 30px rgba(0,0,0,0.18);
    overflow: hidden;
  }
  .card--front { left: 40px; background: var(--card-dark); }
  .card--back  { left: 615px; background: var(--card-light); }

  /* front */
  .front-brand {
    position: absolute; left: 0; right: 0; top: 118px;
    text-align: center;
  }
  .front-brand__name {
    font-size: 46px; font-weight: 500; letter-spacing: 4px;
    color: var(--silver); text-transform: uppercase;
  }
  .front-brand__web {
    margin-top: 18px;
    font-size: 15px; letter-spacing: 7px; color: var(--silver-soft);
  }

  /* back */
  .back-portrait {
    position: absolute; right: 0; top: 0; bottom: 0; width: 230px;
    background: linear-gradient(90deg, rgba(230,216,208,0) 0%, var(--skin-warm) 45%, #dccbc2 100%);
  }
  .back-brand {
    position: absolute; left: 0; right: 0; top: 78px;
    display: flex; justify-content: center; align-items: center; gap: 10px;
  }
  .back-brand__mark {
    width: 12px; height: 12px; border-radius: 50%; background: var(--brand-blue);
  }
  .back-brand__name {
    font-size: 30px; font-weight: 500; letter-spacing: 3px;
    color: var(--brand-blue); text-transform: uppercase;
  }
  .locations {
    position: absolute; left: 40px; right: 40px; top: 170px;
    display: flex; gap: 36px;
  }
  .location {
    flex: 1; font-size: 15px; line-height: 1.45; color: var(--ink);
    font-style: normal;
  }
  .location--rotterdam { text-align: right; }
  .location--amsterdam { text-align: left; }
</style>
</head>
<body>
<main class="sheet">
  <section class="card card--front" aria-label="Voorzijde visitekaartje">
    <div class="front-brand">
      <div class="front-brand__name">Velora Huid</div>
      <div class="front-brand__web">www.velorahuid.nu</div>
    </div>
  </section>

  <section class="card card--back" aria-label="Achterzijde visitekaartje">
    <div class="back-portrait" role="img" aria-label="Zachte portretfoto van een vrouw met verzorgde huid"></div>
    <div class="back-brand">
      <span class="back-brand__mark"></span>
      <span class="back-brand__name">Velora Huid</span>
    </div>
    <div class="locations">
      <address class="location location--rotterdam">
        Lindenhofkade 42B<br>
        3017KP Rotterdam<br>
        Tel 010 438 21 95<br>
        www.velorahuid.nu
      </address>
      <address class="location location--amsterdam">
        Zonnewijzerstraat 73<br>
        1062HT Amsterdam<br>
        Tel 020 519 8372<br>
        info@velorahuid.nu
      </address>
    </div>
  </section>
</main>
</body>
</html>
```